One Page flat design for Car Classified Site

I'm looking for a flat design that that is very simple on the eye but with style. I need it to have a footer for some links etc, and the header needs a new feel but nothing to major.
This one page design is needed for the main page of the classified site...after this page is correct then all the other pages need to be designed to follow a similar style (new work).
I want more emphasis on the text rather than the images as a lot of users don't add images of the vehicles.
Attached is a mock up of the information and rough layout.
Wheelmarketlane.com is a classified site for car dealers only, I've also attached how the main competitions site looks.
Target Market(s)
Middle aged men, these guys are car dealers so it needs to be basic and easy for them as they aren't techie types.
Industry/Entity Type
Work
Number of Pages Required
1 page
Font styles to use
Look and feel

```html
<!DOCTYPE html>
<html lang="en">
<head>
<meta charset="utf-8">
<title>Wheelmarketlane.com – Search Results</title>
<link href="https://fonts.googleapis.com/css2?family=Carlito:ital,wght@0,400;0,700;1,400&display=swap" rel="stylesheet">
<style>
  :root {
    --brand: #fbb000;
    --ink: #111111;
    --black: #0a0a0a;
    --panel: #f4f4f4;
    --card: #f5f5f5;
    --line: #dcdcdc;
    --muted: #a8a8a8;
    --white: #ffffff;
  }
  * { box-sizing: border-box; margin: 0; padding: 0; }
  html, body { width: 889px; height: 1200px; overflow: hidden; }
  body {
    position: relative;
    background: var(--white);
    font-family: "Carlito", "Calibri", sans-serif;
    color: var(--ink);
  }
  .abs { position: absolute; }

  /* Header */
  .top-rule { left: 0; top: 25px; width: 889px; height: 1px; background: var(--line); }
  .main-nav { top: 6px; left: 619px; display: flex; align-items: center; gap: 18px; font-size: 10px; }
  .social { display: flex; gap: 3px; margin-left: -8px; }
  .social span { width: 11px; height: 11px; border-radius: 50%; background: #555; display: block; }
  .login-row { top: 28px; left: 386px; display: flex; align-items: center; font-size: 10px; }
  .login-row .field {
    height: 17px; border: 1px solid var(--line); background: #fafafa;
    padding: 2px 8px; font-size: 9.5px; color: #333;
  }
  .login-label { margin-right: 9px; }
  .field.user { width: 146px; margin-right: 7px; }
  .field.pass { width: 146px; margin-right: 9px; }
  .login-btn { color: var(--brand); font-size: 10px; }
  .header-band { left: 0; top: 47px; width: 889px; height: 30px; background: var(--black); }
  .brand-mark {
    left: 127px; top: 0; width: 77px; height: 86px; background: var(--brand);
    display: flex; align-items: center; justify-content: center; text-align: center;
    font-size: 13px; line-height: 1.05; color: var(--ink); padding: 0 4px;
  }
  .header-foot { left: 0; top: 100px; width: 889px; height: 1px; background: var(--line); }

  /* Search panel */
  .search-panel { left: 0; top: 101px; width: 889px; height: 209px; background: var(--panel); border-bottom: 1px solid var(--line); }
  .select {
    width: 304px; height: 30px; background: var(--white); border: 1px solid #e2e2e2;
    font-style: italic; font-size: 11.5px; color: var(--brand); padding: 9px 9px;
  }
  .select::after {
    content: ""; position: absolute; right: 9px; top: 13px;
    border-left: 3.5px solid transparent; border-right: 3.5px solid transparent; border-top: 6px solid var(--ink);
  }
  .adv-btn {
    left: 640px; top: 272px; width: 124px; height: 27px; background: var(--brand);
    border: 2px solid var(--ink); border-radius: 2px; color: var(--white);
    font-style: italic; font-size: 11.5px; text-align: center; line-height: 23px;
  }

  .results-title { left: 127px; top: 335px; font-size: 19.5px; }

  /* Listing cards */
  .listing { left: 127px; width: 636px; border: 1px solid var(--line); background: var(--card); }
  .listing-head {
    height: 32px; background: var(--brand); position: relative;
    display: flex; align-items: center; padding-left: 13px;
  }
  .listing-title { font-size: 18px; letter-spacing: 0.1px; }
  .tag { position: absolute; top: 9px; color: var(--white); font-size: 11.5px; display: flex; align-items: center; gap: 5px; }
  .tag.viewed { left: 290px; }
  .tag.featured { left: 362px; }
  .buy-line { position: absolute; right: 6px; top: 11px; font-size: 11.5px; }
  .listing-body { position: relative; height: 165px; }
  .photo {
    position: absolute; left: 20px; top: 14px; width: 93px; height: 70px; background: var(--white);
    color: #c8c8c8; font-size: 10.5px; display: flex; align-items: center; justify-content: center;
  }
  .specs, .dealer { position: absolute; font-size: 11.5px; line-height: 15.3px; }
  .specs { left: 130px; top: 17px; }
  .dealer { left: 253px; top: 12px; }
  .pricing { position: absolute; left: 461px; top: 15px; font-size: 11.5px; width: 170px; }
  .pricing h3 { font-size: 11.5px; font-weight: 700; margin-bottom: 2px; }
  .price-grid { display: grid; grid-template-columns: 93px 77px; line-height: 15px; }
  .price-grid .value { color: var(--brand); }
  .comments { position: absolute; left: 20px; top: 97px; width: 608px; }
  .comments h4 { font-weight: 400; font-size: 11.5px; line-height: 13px; }
  .comments p { font-size: 8.3px; line-height: 11px; }
  .more-btn {
    position: absolute; left: 469px; top: 134px; width: 120px; height: 23px;
    background: var(--brand); font-size: 13px; text-align: center; line-height: 23px;
  }

  /* Footer */
  .footer-rule { left: 20px; top: 1059px; width: 869px; height: 1px; background: var(--line); }
  .footer { left: 6px; top: 1064px; width: 883px; height: 30px; background: var(--black); }
  .footer-links { position: absolute; left: 306px; top: 11px; display: flex; gap: 10px; font-size: 9px; color: var(--white); }
</style>
</head>
<body>

<header>
  <div class="abs top-rule"></div>
  <nav class="abs main-nav">
    <span>Home</span>
    <span>Watch List</span>
    <span class="social" aria-label="Social links"><span></span><span></span><span></span><span></span></span>
  </nav>
  <div class="abs login-row">
    <span class="login-label">Login Here</span>
    <span class="field user">Enter Username</span>
    <span class="field pass">Enter Password</span>
    <span class="login-btn">LOGIN</span>
  </div>
  <div class="abs header-band"></div>
  <div class="abs brand-mark">Wheel&shy;market&shy;lane</div>
  <div class="abs header-foot"></div>
</header>

<section class="abs search-panel" aria-label="Search">
</section>
<div class="abs select" style="left:127px;top:135px;">Enter Make</div>
<div class="abs select" style="left:458px;top:135px;">Enter Model</div>
<div class="abs select" style="left:127px;top:184px;">Enter Price</div>
<div class="abs select" style="left:458px;top:184px;">Enter Age</div>
<div class="abs select" style="left:127px;top:233px;">Enter Body type</div>
<div class="abs select" style="left:458px;top:233px;">Enter a keyword</div>
<div class="abs adv-btn">Advance Search</div>

<h2 class="abs results-title" style="font-weight:400;">Search Results listed below:</h2>

<!-- Listing 1 -->
<article class="abs listing" style="top:374px;">
  <div class="listing-head">
    <h2 class="listing-title" style="font-weight:400;">2013 NORVAL KESTREL VISTA DTI</h2>
    <span class="tag viewed"><svg width="10" height="9" viewBox="0 0 10 9"><path d="M1 5 L4 8 L9 1" fill="none" stroke="#fff" stroke-width="2"/></svg>Viewed</span>
    <span class="tag featured"><svg width="11" height="11" viewBox="0 0 24 24"><path d="M12 2l3 7h7l-5.6 4.6L18.5 21 12 16.8 5.5 21l2.1-7.4L2 9h7z" fill="#fff"/></svg>Featured</span>
    <span class="buy-line">Buy it for $13570 or Please a Bid</span>
  </div>
  <div class="listing-body">
    <div class="photo" role="img" aria-label="Vehicle photo">image</div>
    <div class="specs">2014<br>96000 Miles<br>Automatic<br>Black</div>
    <div class="dealer">Ridgeway Motors UK<br>127 Miles Away</div>
    <div class="pricing">
      <h3>Trying to deal my customer</h3>
      <div class="price-grid"><span>Trade Price</span><span>Retail Price</span><span class="value">$14,500</span><span class="value">$16,900</span></div>
    </div>
    <div class="comments">
      <h4>Dealer Comments:</h4>
      <p>Prepared for retail, Norval GB plus 1 private owner, serviced twice at Norval at 7k and 18k-- 2keys available. Not yet due an MOT Prepared for retail, Norval GB plus 1 private owner, serviced twice at Norval at 7k and 18k-- 2keys available. Not yet due an MOT</p>
    </div>
    <div class="more-btn">More Information</div>
  </div>
</article>

<!-- Listing 2 -->
<article class="abs listing" style="top:603px;">
  <div class="listing-head">
    <h2 class="listing-title" style="font-weight:400;">2013 NORVAL KESTREL VISTA DTI</h2>
    <span class="tag viewed"><svg width="10" height="9" viewBox="0 0 10 9"><path d="M1 5 L4 8 L9 1" fill="none" stroke="#fff" stroke-width="2"/></svg>Viewed</span>
    <span class="tag featured"><svg width="11" height="11" viewBox="0 0 24 24"><path d="M12 2l3 7h7l-5.6 4.6L18.5 21 12 16.8 5.5 21l2.1-7.4L2 9h7z" fill="#fff"/></svg>Featured</span>
    <span class="buy-line">Buy it for $13570 or Please a Bid</span>
  </div>
  <div class="listing-body" style="height:164px;">
    <div class="photo" style="top:24px;" role="img" aria-label="Vehicle photo">image</div>
    <div class="specs" style="top:21px;">2014<br>96000 Miles<br>Automatic<br>Black</div>
    <div class="dealer" style="top:21px;">Ridgeway Motors UK<br>127 Miles Away</div>
    <div class="pricing" style="top:20px;">
      <h3>Trying to deal my customer</h3>
      <div class="price-grid"><span>Trade Price</span><span>Retail Price</span><span class="value">$14,500</span><span class="value">$16,900</span></div>
    </div>
    <div class="comments">
      <h4>Dealer Comments:</h4>
      <p>Prepared for retail, Norval GB plus 1 private owner, serviced twice at Norval at 7k and 18k-- 2keys available. Not yet due an MOT Prepared for retail, Norval GB plus 1 private owner, serviced twice at Norval at 7k and 18k-- 2keys available. Not yet due an MOT</p>
    </div>
    <div class="more-btn">More Information</div>
  </div>
</article>

<!-- Listing 3 -->
<article class="abs listing" style="top:832px;">
  <div class="listing-head">
    <h2 class="listing-title" style="font-weight:400;">2013 NORVAL KESTREL VISTA DTI</h2>
    <span class="buy-line">Buy it for $13570 or Please a Bid</span>
  </div>
  <div class="listing-body">
    <div class="photo" style="top:19px;" role="img" aria-label="Vehicle photo">image</div>
    <div class="specs" style="top:16px;">2014<br>96000 Miles<br>Automatic<br>Black</div>
    <div class="dealer" style="top:16px;">Ridgeway Motors UK<br>127 Miles Away</div>
    <div class="pricing" style="top:17px;">
      <h3>Trying to deal my customer</h3>
      <div class="price-grid"><span>Trade Price</span><span>Retail Price</span><span class="value">$14,500</span><span class="value">$16,900</span></div>
    </div>
    <div class="comments" style="top:96px;">
      <h4>Dealer Comments:</h4>
      <p>Prepared for retail, Norval GB plus 1 private owner, serviced twice at Norval at 7k and 18k-- 2keys available. Not yet due an MOT Prepared for retail, Norval GB plus 1 private owner, serviced twice at Norval at 7k and 18k-- 2keys available. Not yet due an MOT</p>
    </div>
    <div class="more-btn" style="top:136px;">More Information</div>
  </div>
</article>

<footer>
  <div class="abs footer-rule"></div>
  <div class="abs footer">
    <nav class="footer-links">
      <span>Contact us</span><span>About us</span><span>Legal info</span><span>Privacy Policy</span><span>Terms &amp; Conditions</span>
    </nav>
  </div>
</footer>

</body>
</html>
```